Business card design for online Mandarin Learning School

We need a business card design for our online language learning school called "Sunny Kite Academy for Mandarin Learning". Our existing website is https://www.sunnykiteacademy.com
We have our logo already. We would like to see our business card design that can make our online teaching services to be innovative, young, energetic and fun to learn. Prefer to have a certain level of color matching with our website. Apart from "Sunny Kite Academy", need to specifically state "for Mandarin Learning" as well on the business card.

```html
<!DOCTYPE html>
<html lang="en">
<head>
<meta charset="utf-8">
<title>Sunny Kite Academy – Business Card</title>
<link rel="stylesheet" href="https://fonts.googleapis.com/css2?family=Cinzel:wght@400&family=Arimo:wght@400;700&display=swap">
<style>
  :root {
    --teal: #1fabb6;
    --teal-dark: #14a1ae;
    --coral: #e05c5c;
    --grey: #8a8a8a;
    --ink: #5f5f5f;
    --white: #ffffff;
    --stage: #e9ecee;
  }
  * { box-sizing: border-box; margin: 0; padding: 0; }
  html, body { width: 1200px; height: 880px; overflow: hidden; }
  body {
    background: var(--stage);
    display: flex; flex-direction: column; align-items: center; justify-content: center;
    gap: 40px;
  }
  .card {
    position: relative; width: 700px; height: 400px; border-radius: 22px;
    overflow: hidden; box-shadow: 0 6px 20px rgba(0,0,0,.12);
  }
  /* Front */
  .card--front { background: var(--teal); color: var(--white); display: flex; align-items: center; justify-content: center; }
  .front-brand { text-align: center; font-family: "Cinzel", serif; }
  .front-brand__name { font-size: 52px; letter-spacing: 1px; line-height: 1; padding: 0 6px 8px; border-bottom: 4px solid var(--white); }
  .front-brand__url { font-size: 22px; letter-spacing: .5px; margin-top: 8px; }
  /* Back */
  .card--back { background: var(--white); font-family: "Arimo", sans-serif; }
  .brand {
    position: absolute; left: 40px; top: 170px; width: 300px;
    display: flex; align-items: center; gap: 12px;
    font-family: "Cinzel", serif; color: var(--teal); font-size: 27px; line-height: 1.1;
  }
  .brand__dot { flex: none; width: 22px; height: 22px; border-radius: 50%; background: var(--coral); }
  .divider { position: absolute; left: 372px; top: 80px; width: 1px; height: 170px; background: var(--teal); }
  .contact { position: absolute; left: 400px; top: 60px; color: var(--ink); font-size: 15px; line-height: 1.3; }
  .contact__name { color: var(--teal-dark); font-weight: 700; font-size: 24px; line-height: 1; }
  .contact__role { font-size: 15px; margin-bottom: 12px; }
  .contact__address { margin-bottom: 10px; }
  .contact__row { display: flex; align-items: center; gap: 8px; }
  .contact__row svg { width: 12px; height: 12px; flex: none; }
  .band { position: absolute; left: 0; right: 0; bottom: 48px; height: 32px; display: flex; }
  .band span { height: 100%; }
  .band .g { background: var(--grey); }
  .band .c { background: var(--coral); }
  .band .t { background: var(--teal); }
  .band__text {
    position: absolute; left: 200px; right: 100px; bottom: 48px; height: 32px;
    display: flex; align-items: center; justify-content: space-between;
    color: var(--white); font-weight: 700; font-size: 17px;
  }
</style>
</head>
<body>
  <section class="card card--front">
    <div class="front-brand">
      <div class="front-brand__name">SUNNY KITE ACADEMY</div>
      <div class="front-brand__url">WWW.SUNNYKITEACADEMY.COM</div>
    </div>
  </section>

  <section class="card card--back">
    <div class="brand"><span class="brand__dot"></span><span>Sunny Kite Academy</span></div>
    <div class="divider"></div>
    <div class="contact">
      <div class="contact__name">Lena Moore</div>
      <div class="contact__role">Director</div>
      <div class="contact__address">PO BOX 481, Kite Lane<br>Harbour Road Brightwater</div>
      <div class="contact__row">
        <svg viewBox="0 0 12 12"><path d="M2 1 L4.5 1 L5.5 3.5 L4 4.5 Q5 7 7.5 8 L8.5 6.5 L11 7.5 L11 10 Q6 11 2 6 Q1 3.5 2 1Z" fill="var(--teal)"/></svg>
        <span>(555) 018 2046</span>
      </div>
      <div class="contact__row">
        <svg viewBox="0 0 12 12"><rect x="0.5" y="2" width="11" height="8" fill="var(--teal)"/><path d="M0.5 2 L6 7 L11.5 2" stroke="#fff" fill="none"/></svg>
        <span>hello@sunnykitemail.com</span>
      </div>
      <div class="contact__row">
        <svg viewBox="0 0 12 12"><circle cx="6" cy="6" r="5.5" fill="var(--teal)"/><path d="M0.5 6 H11.5 M6 0.5 V11.5 M6 0.5 Q2.5 6 6 11.5 M6 0.5 Q9.5 6 6 11.5" stroke="#fff" stroke-width=".7" fill="none"/></svg>
        <span>www.sunnykiteacademy.com</span>
      </div>
    </div>
    <div class="band" aria-hidden="true">
      <span class="g" style="width:170px"></span>
      <span class="c" style="width:110px"></span>
      <span class="t" style="width:180px"></span>
      <span class="c" style="width:60px"></span>
      <span class="t" style="width:100px"></span>
      <span class="g" style="flex:1"></span>
    </div>
    <div class="band__text">
      <span>F</span><span>o</span><span>r</span><span>&nbsp;</span><span>M</span><span>a</span><span>n</span><span>d</span><span>a</span><span>r</span><span>i</span><span>n</span><span>&nbsp;</span><span>L</span><span>e</span><span>a</span><span>r</span><span>n</span><span>i</span><span>n</span><span>g</span>
    </div>
  </section>
</body>
</html>
```